Veltarum

Standard Business Card design.
Sample two-sided design uploaded. White front, Black back.
Would like white shield to be on all black background side.
Willing to look at a couple creative designs, but nothing crazy.
Preference for a classic, confident, strong design.

```html
<!DOCTYPE html>
<html lang="en">
<head>
<meta charset="utf-8">
<title>Veltarum Business Card</title>
<link rel="stylesheet" href="https://fonts.googleapis.com/css2?family=Oswald:wght@600&family=Poppins:wght@300;400;600&display=swap">
<style>
  :root {
    --stage: #0a0a0a;
    --card-black: #1c1c1d;
    --card-white: #ffffff;
    --ink: #111111;
    --ink-soft: #3a3a3a;
    --silver: #b9b9bb;
  }
  * { margin: 0; padding: 0; box-sizing: border-box; }
  html, body { width: 1200px; height: 886px; overflow: hidden; background: var(--stage); }
  .canvas {
    width: 1200px; height: 886px;
    display: flex; flex-direction: column; align-items: center; justify-content: center; gap: 40px;
  }
  .card {
    width: 600px; height: 343px; position: relative;
    font-family: "Poppins", sans-serif;
  }
  .card--back {
    background: var(--card-black);
    display: flex; align-items: center; justify-content: center;
  }
  .brand {
    display: flex; align-items: center; gap: 10px;
    font-weight: 600; letter-spacing: 0.18em; text-transform: uppercase;
  }
  .brand__mark { display: block; }
  .card--back .brand { color: var(--silver); font-size: 30px; }
  .card--back .brand__mark { width: 18px; height: 18px; background: var(--silver); }
  .card--front { background: var(--card-white); color: var(--ink); }
  .card--front .brand {
    position: absolute; top: 34px; right: 36px;
    font-size: 17px; color: var(--ink);
  }
  .card--front .brand__mark { width: 11px; height: 11px; background: var(--ink); }
  .person { position: absolute; left: 36px; top: 150px; }
  .person__name {
    font-family: "Oswald", sans-serif; font-weight: 600;
    font-size: 27px; letter-spacing: 0.01em; line-height: 1.05; text-transform: uppercase;
  }
  .person__role { font-weight: 300; font-size: 13px; color: var(--ink-soft); }
  .contacts {
    position: absolute; left: 46px; top: 226px;
    border-left: 6px solid var(--ink); padding-left: 14px;
    list-style: none;
  }
  .contacts li {
    display: flex; align-items: center; gap: 12px;
    font-weight: 300; font-size: 14px; line-height: 22px; letter-spacing: 0.03em;
  }
  .contacts svg { width: 13px; height: 13px; fill: var(--ink); flex: none; }
  .address {
    position: absolute; left: 36px; bottom: 12px;
    font-weight: 300; font-size: 12.5px; color: var(--ink-soft); letter-spacing: 0.02em;
  }
</style>
</head>
<body>
<main class="canvas">
  <section class="card card--back" aria-label="Card back">
    <div class="brand"><span class="brand__mark"></span>Veltarum</div>
  </section>

  <section class="card card--front" aria-label="Card front">
    <div class="brand"><span class="brand__mark"></span>Veltarum</div>

    <div class="person">
      <h1 class="person__name">Your Name Here</h1>
      <p class="person__role">Executive Director</p>
    </div>

    <ul class="contacts">
      <li>
        <svg viewBox="0 0 24 24"><path d="M6.6 10.8a15.1 15.1 0 0 0 6.6 6.6l2.2-2.2c.3-.3.7-.4 1-.2 1.1.4 2.3.6 3.6.6.6 0 1 .4 1 1V20c0 .6-.4 1-1 1A17 17 0 0 1 3 4c0-.6.4-1 1-1h3.5c.6 0 1 .4 1 1 0 1.3.2 2.5.6 3.6.1.3 0 .7-.2 1z"/></svg>
        1300581927
      </li>
      <li>
        <svg viewBox="0 0 24 24"><path d="M7 1h10a2 2 0 0 1 2 2v18a2 2 0 0 1-2 2H7a2 2 0 0 1-2-2V3a2 2 0 0 1 2-2zm0 3v15h10V4zm5 16.2a1 1 0 1 0 0 2 1 1 0 0 0 0-2z"/></svg>
        7252009614
      </li>
      <li>
        <svg viewBox="0 0 24 24"><path d="M2 5h20v14H2zm2 2v.4l8 5.3 8-5.3V7zm0 2.8V17h16V9.8l-8 5.3z"/></svg>
        info@veltarum.co.in
      </li>
      <li>
        <svg viewBox="0 0 24 24"><path d="M12 2a10 10 0 1 0 0 20 10 10 0 0 0 0-20zm6.9 6h-2.9a15.6 15.6 0 0 0-1.4-3.6A8 8 0 0 1 18.9 8zM12 4c.8 1.2 1.5 2.5 1.9 4h-3.8c.4-1.4 1.1-2.8 1.9-4zM4.3 14a8 8 0 0 1 0-4h3.4a16 16 0 0 0 0 4zm.8 2h2.9c.3 1.3.8 2.5 1.4 3.6A8 8 0 0 1 5.1 16zM8 8H5.1a8 8 0 0 1 4.3-3.6C8.8 5.5 8.3 6.7 8 8zm4 12c-.8-1.2-1.5-2.5-1.9-4h3.8c-.4 1.4-1.1 2.8-1.9 4zm2.3-6H9.7a14.7 14.7 0 0 1 0-4h4.6a14.7 14.7 0 0 1 0 4zm.3 5.6c.6-1.1 1.1-2.3 1.4-3.6h2.9a8 8 0 0 1-4.3 3.6zm1.7-5.6a16 16 0 0 0 0-4h3.4a8 8 0 0 1 0 4z"/></svg>
        www.veltarum.co.in
      </li>
    </ul>

    <p class="address">your address near Keshav chowk Ravipur Nandgiri</p>
  </section>
</main>
</body>
</html>
```